Print & digital package needed for technology firm

We need a package of coordinating marketing materials for our technology business. We offer technology solutions to midsized organizations, including data center, outsourced IT, and technology consulting. Find more information on our website, www.pexlora.com. Design is the main concern, we can modify the text ongoing to best reflect our company’s offerings. The design should communicate technology expertise and strategic thinking. Our website is currently being updated with a “flat design” theme and we’d like design of these items to be flat, fresh, modern, and professional, without being boring.
Please use attached logo - can send in .ai/.eps/.psd/etc. Fonts in logo are Futura, Futura Book, and Lato. Please use pexLORA blue, #0372bb.
Please find attached one of our product flyers for one of the computers we lease. Fonts used are Roboto Slab (partial to this font) & Lato. Also attached copy of our business card design.
Taglines we have used include “Does IT hear what troubles you?” and “IT made simple” although we are open to new ideas.
Would like final products to be available in editable files - .psd/.tif/.ai/etc.

- 1 PowerPoint template
- 1 leaderboard ad (digital, 72dpi)
- 1 medium rectangle ad 300x250 (digital, 72dpi)
- 1 full page ad 8x11 (print, 300dpi)
- 1 half-page ad horizontal (print, 300dpi)
- 1 letterhead template
- 1 proposal front-page

There is potential for further graphic/print design opportunities for our business as well.

All, thank you for your assistance in understanding the budget process with this type of design contest - we have updated the project's budget to reflect the items we are requesting.

Please email mvarga at pexlora.com with inquiries or comments. Thank you.

Designers,

Due to an oversight, our project was listed as "refundable" - this has been corrected and changed to committed payment.
To enter into this contest, please pick 2-3 items from the list of desired materials (ads, powerpoint, letterhead, etc.) It is not necessary to submit all items which will be part of the final package to be considered for the contest.

Thank you. Please contact mvarga@pexlora.com for questions.
Best,
Mimi

CEOs, CFOs, CIOs, COOs - college+ educated, 30-60, professional.

```html
<!DOCTYPE html>
<html lang="en">
<head>
<meta charset="utf-8">
<title>pexLORA presentation template</title>
<link rel="stylesheet" href="https://fonts.googleapis.com/css2?family=Jost:wght@400;500;600&family=Roboto+Slab:wght@400;600;700&display=swap">
<style>
:root{
  --brand-blue:#0372bb;
  --brand-navy:#163b5e;
  --ink:#3a3a3a;
  --ink-dark:#2f2f2f;
  --orange:#f39a1e;
  --paper:#ffffff;
  --stage:#ffffff;
  --rule:#5fa0d6;
  --text:#111111;
  --heading-font:"Roboto Slab",serif;
  --body-font:"Jost",sans-serif;
}
*{box-sizing:border-box;margin:0;padding:0}
html,body{width:1200px;height:1000px;overflow:hidden;background:var(--stage)}
.canvas{position:relative;width:1200px;height:1000px}
.slide{position:absolute;width:520px;height:420px;background:var(--paper);overflow:hidden;border:1px solid #e3e3e3}
.slide--section{left:25px;top:25px}
.slide--content{left:400px;top:245px}
.slide--contents{left:665px;top:560px}
.slide__topbar{position:absolute;left:0;top:0;width:100%;height:24px;background:var(--ink)}
.slide__footer{position:absolute;left:0;bottom:0;width:100%;height:14px;background:var(--brand-blue)}
.brand-tab{position:absolute;right:0;top:0;height:34px;padding:0 10px 0 14px;background:var(--ink);border-bottom-left-radius:8px;display:flex;align-items:center;font-family:var(--body-font);font-weight:500;font-size:12px;color:#fff}
.brand-tab--low{top:24px}
.pattern-field{position:absolute;left:0;bottom:14px;border-top-right-radius:100% 100%;background:radial-gradient(circle at 0% 100%,rgba(3,114,187,.22) 0%,rgba(3,114,187,.10) 45%,rgba(3,114,187,0) 75%)}
.pattern-field--section{width:420px;height:340px}
.pattern-field--contents{width:380px;height:330px;opacity:.7}
.photo{position:absolute;border-radius:50%;border:2px solid var(--brand-blue);background:#fff;padding:3px}
.photo span{display:block;width:100%;height:100%;border-radius:50%}
.photo--server span{background:linear-gradient(135deg,#e9edf1,#4a4f57)}
.photo--laptop span{background:linear-gradient(160deg,#f2f2f2,#2b2d31)}
.photo--person span{background:linear-gradient(140deg,#e6e1d8,#a89a82)}
.photo--storage span{background:linear-gradient(150deg,#f0e2c6,#c98b3b)}
.section-number{position:absolute;right:26px;top:108px;width:26px;height:26px;border-radius:50%;background:var(--ink-dark);color:#fff;font-family:var(--heading-font);font-weight:700;font-size:14px;display:flex;align-items:center;justify-content:center}
.section-band{position:absolute;right:0;top:142px;width:170px;height:30px;background:var(--brand-blue);clip-path:polygon(6% 0,100% 0,100% 100%,0 100%);color:#fff;font-family:var(--heading-font);font-weight:700;font-size:17px;display:flex;align-items:center;justify-content:flex-end;padding-right:18px}
.title-band{position:absolute;left:0;top:72px;width:310px;height:30px;background:linear-gradient(90deg,#fff 0%,var(--brand-blue) 30%,var(--brand-blue) 70%,var(--brand-navy) 100%);clip-path:polygon(0 0,97% 0,100% 100%,0 100%);color:#fff;font-family:var(--heading-font);font-weight:700;font-size:19px;text-align:center;line-height:30px}
.title-band--twoline{top:106px;width:240px;height:28px;background:var(--ink);font-size:9px;line-height:10px;padding-top:4px;clip-path:polygon(0 0,96% 0,100% 100%,0 100%)}
.subtitle-band{position:absolute;left:48px;top:140px;width:190px;height:24px;background:var(--orange);clip-path:polygon(4% 0,100% 0,100% 100%,0 100%);color:#fff;font-family:var(--heading-font);font-weight:600;font-size:14px;text-align:center;line-height:24px}
.column{position:absolute;font-family:var(--body-font);font-weight:500;font-size:9.6px;line-height:11.4px;color:var(--text);text-align:justify;text-align-last:center;border-top:1px solid var(--rule);padding-top:10px}
.column--left{left:14px;top:170px;width:232px}
.column--right{left:262px;top:196px;width:238px}
.contents-band{position:absolute;right:0;top:128px;width:250px;height:22px;background:linear-gradient(90deg,#fff 0%,var(--brand-blue) 25%,var(--brand-blue) 65%,#1f2f40 100%);color:#fff;font-family:var(--heading-font);font-weight:700;font-size:14px;line-height:22px;padding-left:96px}
.contents-list{position:absolute;left:262px;top:175px;list-style:none;font-family:var(--body-font);font-weight:500;font-size:10px;color:var(--text)}
.contents-list li{display:flex;align-items:center;height:37px}
.contents-list b{width:24px;height:24px;border-radius:4px;background:var(--ink-dark);color:#fff;font-family:var(--heading-font);font-weight:700;font-size:13px;display:flex;align-items:center;justify-content:center;margin-right:22px}
</style>
</head>
<body>
<div class="canvas">

  <section class="slide slide--section">
    <div class="slide__topbar"></div>
    <div class="brand-tab">pexlora.com</div>
    <div class="pattern-field pattern-field--section" role="img" aria-label="Decorative fan of thin blue curved lines radiating from the lower left corner"></div>
    <div class="photo photo--server" style="left:14px;top:105px;width:70px;height:70px" role="img" aria-label="Photo: technician beside a server rack"><span></span></div>
    <div class="photo photo--laptop" style="left:58px;top:158px;width:84px;height:84px" role="img" aria-label="Photo: open laptop"><span></span></div>
    <div class="photo photo--person" style="left:66px;top:240px;width:86px;height:86px" role="img" aria-label="Photo: businessman at an office desk"><span></span></div>
    <div class="photo photo--storage" style="left:32px;top:318px;width:68px;height:68px" role="img" aria-label="Photo: data storage units"><span></span></div>
    <div class="section-number">1</div>
    <div class="section-band">part A</div>
    <div class="slide__footer"></div>
  </section>

  <section class="slide slide--content">
    <div class="slide__topbar"></div>
    <div class="brand-tab brand-tab--low">pexlora.com</div>
    <h1 class="title-band">Title</h1>
    <h2 class="title-band title-band--twoline">2 Line<br>Title</h2>
    <h3 class="subtitle-band">Subtitle</h3>
    <p class="column column--left">Lorem ipsum dolor sit amet, pellentesque mauris ligula magna ut. Mauris duis pretium, vitae in ad viverra, dictum placerat. Turpis nunc. Vestibulum est cras, donec in suscipit, vitae ut feugiat. Non maxime, ipsum suspendisse consectetuer. Donec id aliquam nulla arcu, orci inceptos metus molestie lorem quis, sed orci lacus, vestibulum sit. Aenean ut tellus volutpat, orci nec cum justo tortor, convallis lorem nostra ipsum eget. Imperdiet maecenas quis fermentum, eget donec felis mi orci justo aliquet. Lectus viverra donec nunc quam commodo, conubia risus. Vitae sagittis lacus ullamcorper sagittis nec ultricies, elit cursus consequat faucibus nam ac est. Tellus viverra, nostra integer, tellus mollis sint, in commodo eu ultrices, turpis facilisi ut velit. Wisi phasellus aliquam, ut neque lacus consequat dictum ut, accumsan vestibulum nibh morbi pellentesque lorem, beatae est accumsan eu sit placerat in, lacinia nibh nam elit.</p>
    <p class="column column--right">Lorem ipsum dolor sit amet, pellentesque mauris ligula magna ut. Mauris duis pretium, vitae in ad viverra, dictum placerat. Turpis nunc. Vitae sagittis lacus ullamcorper sagittis nec ultricies, elit cursus consequat faucibus nam ac est. Tellus viverra, nostra integer, tellus mollis sint, in commodo eu ultrices, turpis facilisi ut velit. Wisi phasellus aliquam, ut neque lacus consequat dictum ut, accumsan vestibulum nibh morbi pellentesque lorem, beatae est accumsan eu sit placerat in, lacinia nibh nam elit.</p>
    <div class="slide__footer"></div>
  </section>

  <section class="slide slide--contents">
    <div class="slide__topbar"></div>
    <div class="brand-tab">pexlora.com</div>
    <div class="pattern-field pattern-field--contents" role="img" aria-label="Decorative fan of faint blue curved lines radiating from the lower left corner"></div>
    <div class="photo photo--server" style="left:10px;top:84px;width:68px;height:68px" role="img" aria-label="Photo: technician beside a server rack"><span></span></div>
    <div class="photo photo--laptop" style="left:52px;top:136px;width:84px;height:84px" role="img" aria-label="Photo: open laptop"><span></span></div>
    <div class="photo photo--person" style="left:56px;top:222px;width:86px;height:86px" role="img" aria-label="Photo: businessman at an office desk"><span></span></div>
    <div class="photo photo--storage" style="left:20px;top:300px;width:68px;height:68px" role="img" aria-label="Photo: data storage units"><span></span></div>
    <h1 class="contents-band">Contents</h1>
    <ol class="contents-list">
      <li><b>1</b>Part A</li>
      <li><b>2</b>Part B</li>
      <li><b>3</b>Part C</li>
      <li><b>4</b>Part D</li>
      <li><b>5</b>Part E</li>
    </ol>
    <div class="slide__footer"></div>
  </section>

</div>
</body>
</html>
```